Natural Health Supplement Company Needs a Product Label Designed

HARVEST ROOT LABS needs a PROBIOTICS product label designed.We are a natural health vitamin and dietary supplement company. Who ever wins will have the opportunity to design a lot more product labels for us.
Product name: PROBIOTICS
*Please use the attached logo and base the label text exactly off the Kelt Wellness label example.
Other product examples have been attached for inspiration.

Colors

Designer to choose colors to be used in the design.

Requirements
Must have
• Product name: PROBIOTICS
• *Please use the attached logo and base the label text exactly off the Kelt Wellness label example.
• Other product examples have been attached for inspiration.

```html
<!DOCTYPE html>
<html lang="en">
<head>
<meta charset="utf-8">
<title>Harvest Root Labs – Probiotics Label</title>
<link rel="stylesheet" href="https://fonts.googleapis.com/css2?family=Archivo:wght@600;700;800&family=Russo+One&display=swap">
<style>
  :root {
    --paper: #ffffff;
    --leaf: #8cc63f;
    --leaf-deep: #3fae3a;
    --lime: #c8dc3c;
    --mint: #3fbf8f;
    --teal: #6ccfc0;
    --ink: #4a4a4a;
    --white: #ffffff;
  }
  * { margin: 0; padding: 0; box-sizing: border-box; }
  html, body { width: 1200px; height: 644px; overflow: hidden; background: var(--paper); }
  .label {
    position: relative;
    width: 1200px;
    height: 644px;
    background: var(--paper);
    font-family: "Archivo", Arial, sans-serif;
    overflow: hidden;
  }
  .wash {
    position: absolute;
    left: 470px;
    top: 190px;
    width: 760px;
    height: 500px;
    background:
      radial-gradient(ellipse 320px 210px at 340px 320px, #3fbf8f 0, #45c08a 60%, rgba(63,191,143,0) 100%),
      radial-gradient(ellipse 170px 140px at 160px 290px, #6ccfc0 0, rgba(108,207,192,.9) 45%, rgba(108,207,192,0) 100%),
      radial-gradient(ellipse 230px 240px at 610px 250px, #8cc63f 0, rgba(140,198,63,.9) 50%, rgba(140,198,63,0) 100%),
      radial-gradient(ellipse 290px 170px at 460px 110px, #c8dc3c 0, rgba(200,220,60,.85) 45%, rgba(200,220,60,0) 100%);
    filter: blur(2px);
  }
  .brand {
    position: absolute;
    top: 112px;
    left: 0;
    width: 1200px;
    display: flex;
    justify-content: center;
    align-items: center;
    gap: 12px;
  }
  .brand-dot { width: 22px; height: 22px; border-radius: 50%; background: var(--leaf); }
  .brand-name {
    font-weight: 700;
    font-size: 30px;
    letter-spacing: 3px;
    color: var(--leaf);
  }
  .product-name {
    position: absolute;
    top: 208px;
    left: 0;
    width: 1200px;
    text-align: center;
    font-family: "Russo One", Arial, sans-serif;
    font-size: 76px;
    line-height: 1;
    letter-spacing: 1px;
    color: var(--leaf-deep);
  }
  .strength {
    position: absolute;
    left: 380px;
    top: 300px;
    width: 442px;
    height: 69px;
    border-radius: 35px;
    background: linear-gradient(90deg, #8fca4a, #7cc244);
    display: flex;
    align-items: center;
    justify-content: center;
    color: var(--white);
    font-weight: 800;
    font-size: 42px;
    letter-spacing: 1px;
    text-shadow: 0 2px 3px rgba(0,0,0,.25);
  }
  .claims {
    position: absolute;
    left: 577px;
    top: 440px;
    list-style: none;
    color: var(--white);
    font-weight: 700;
    font-size: 20px;
    line-height: 24px;
    text-shadow: 0 1px 3px rgba(0,0,0,.35);
  }
  .claims li { position: relative; padding-left: 22px; margin-bottom: 16px; }
  .claims li::before {
    content: "";
    position: absolute;
    left: 0; top: 6px;
    width: 12px; height: 12px;
    border-radius: 50%;
    background: var(--white);
    box-shadow: 0 1px 2px rgba(0,0,0,.25);
  }
  .count {
    position: absolute;
    left: 357px;
    top: 558px;
    display: flex;
    align-items: center;
    gap: 8px;
    color: var(--ink);
  }
  .count-number { font-weight: 700; font-size: 40px; line-height: 1; }
  .count-unit { font-weight: 600; font-size: 15px; line-height: 17px; }
  .dots { position: absolute; inset: 0; pointer-events: none; }
</style>
</head>
<body>
<main class="label">
  <div class="wash" role="img" aria-label="Soft green, lime and teal watercolour wash"></div>
  <svg class="dots" width="1200" height="644" aria-hidden="true">
    <circle cx="884" cy="204" r="3" fill="#8cc63f"/>
    <circle cx="1184" cy="250" r="6" fill="#6ccfc0" opacity=".6"/>
    <circle cx="527" cy="566" r="4" fill="#8cc63f"/>
    <circle cx="536" cy="584" r="3" fill="#6ccfc0"/>
  </svg>

  <header class="brand">
    <span class="brand-dot"></span>
    <span class="brand-name">HARVEST ROOT LABS</span>
  </header>

  <h1 class="product-name">PROBIOTICS</h1>
  <div class="strength">50 BILLION CFU</div>

  <ul class="claims">
    <li>Accredited Third-party Tested</li>
    <li>Non-GMO Ingredients</li>
    <li>Support Digestive And<br>Immune System Health</li>
  </ul>

  <div class="count">
    <span class="count-number">60</span>
    <span class="count-unit">VEGETARIANT<br>CAPSULES</span>
  </div>
</main>
</body>
</html>
```